今回のチラシは当社が年4回発行している会報誌に同梱し、DMで直接お客様へ届けるものになります。
対象は庭付一戸建てに住まわれているお客様がほとんどです。なので、セールスワード(安い、お得、今だけ、限定、キャンペーンなど)をちりばめたようなギラギラしたチラシではなく、当社がお客様のお悩みから解放します的な心情に訴えるチラシにしたいです。
お客様のお困りの原因としては、お勤めでなかなか草むしりする時間が取れない、少し前までは自分でやっていたが年で体力的に難しくなった、奥様がマメに手入れしていたが他界してしまい手つかず状態、親が他界して家を相続したが自分は庭に興味なし。お隣さんから苦情が来てしまう。などなど様々です。
庭木が無くても雑草で困っている方にも、気兼ねなく当社にご依頼してもらえるようなイメージのチラシにしたいです。

トップページ
https://www.574k.co.jp/
除草
https://www.574k.co.jp/weeding/
砂利敷き(防草シート含む)
https://www.574k.co.jp/gravel/
表面:キャッチコピー、キャッチコピーに合う写真などの組合せ※情報はこの2つにしてシンプルに。
裏面:社名、支払い方法、フリーダイヤル、URL、QRコードなど ※添付資料参照
A4
両面
シンプル 複雑
単色 カラフル
暗い 明るい
日常 高級
遊び心 厳粛
未来的 伝統的
女性的 男性的
黄・オレンジ系、緑系、茶系
• イラストレーター形式 (.ai)
印刷用のPDFも納品ください。

情報量を少なくしシンプルにまとまっている。
お客様のお困りごとを端的に示していて伝わりやすい。
裏面にある商品説明の記載内容は必要十分の情報量で綺麗に整理されていて読みやすい。

皆様、この度は弊社のチラシ作成に応募いただき誠にありがとうございました。
社内で投票を行いましたが、どれかに集中することなく票がばらける程どれも良い感じだったと思います。
またチラシ作成やその他で募集させていただく際は是非ご応募ください。

```html
<!DOCTYPE html>
<html lang="ja">
<head>
<meta charset="utf-8">
<title>お庭の雑草 お困りではありませんか? | 庭守工房</title>
<link rel="stylesheet" href="https://fonts.googleapis.com/css2?family=M+PLUS+Rounded+1c:wght@500;700;800&family=Noto+Sans+JP:wght@400;500;700;900&display=swap">
<style>
  :root{
    --green:#6fae3a;
    --green-dark:#3f7a22;
    --green-soft:#e6f0d6;
    --orange:#f08a1c;
    --brown:#4a3a2a;
    --cream:#fbfaf3;
    --white:#ffffff;
    --text:#3b3126;
  }
  *{margin:0;padding:0;box-sizing:border-box}
  html,body{width:854px;height:1200px;overflow:hidden;background:var(--white)}
  body{font-family:"Noto Sans JP",sans-serif;color:var(--text)}
  .flyer{position:relative;width:854px;height:1200px;overflow:hidden;background:var(--cream)}
  .hero-photo{position:absolute;left:0;top:0;width:854px;height:820px;
    background:linear-gradient(90deg,#f7f8ef 0%,#eef2df 38%,#9bb46f 62%,#7a6a4c 80%,#5f7a3a 100%)}
  .grass-strip{position:absolute;left:0;top:690px;width:854px;height:130px;
    background:linear-gradient(180deg,rgba(122,170,72,0) 0%,#8fbd57 60%,#79a943 100%)}
  .badge{position:absolute;left:40px;top:26px;width:362px;height:96px;background:var(--green);
    border-radius:14px;color:var(--white);font-family:"M PLUS Rounded 1c",sans-serif;font-weight:800;
    font-size:31px;line-height:40px;text-align:center;padding-top:8px}
  .badge::after{content:"";position:absolute;left:46px;bottom:-18px;border:10px solid transparent;
    border-top:10px solid var(--green);border-left:14px solid var(--green)}
  .headline{position:absolute;left:40px;top:128px;font-family:"M PLUS Rounded 1c",sans-serif;font-weight:800;color:var(--brown)}
  .headline .line1{font-size:74px;line-height:118px;letter-spacing:2px}
  .headline .line1 .accent{color:var(--orange);font-size:112px;vertical-align:-6px}
  .headline .line2{font-size:56px;line-height:72px;letter-spacing:1px}
  .before,.after{position:absolute;border:5px solid var(--white);box-shadow:0 4px 10px rgba(0,0,0,.25)}
  .before{left:28px;top:385px;width:262px;height:300px;background:linear-gradient(160deg,#9a9a92,#6f8a48 55%,#557a2e)}
  .after{left:292px;top:340px;width:310px;height:420px;background:linear-gradient(160deg,#a8a79e,#6e8d46 45%,#8a6a45 80%)}
  .tag{position:absolute;top:-16px;left:-10px;background:var(--green);color:var(--white);font-weight:700;
    font-size:20px;padding:6px 14px;border-radius:16px}
  .arrow{position:absolute;left:248px;top:520px}
  .check-panel{position:absolute;left:28px;top:790px;width:798px;height:285px;background:var(--green-soft);border-radius:10px;overflow:hidden}
  .check-title{height:48px;background:var(--green);color:var(--white);font-weight:700;font-size:26px;line-height:48px;padding-left:28px}
  .check-title .accent{color:#ffe27a}
  .check-list{list-style:none;margin:16px 0 0 20px;width:580px;background:var(--white);border-radius:8px;padding:12px 16px}
  .check-list li{display:flex;align-items:center;gap:10px;font-size:19.5px;font-weight:500;line-height:47px;border-bottom:1px dashed #c9c9b8}
  .check-list li:last-child{border-bottom:none}
  .figure-slot{position:absolute;right:30px;top:70px;width:170px;height:200px;border-radius:10px;
    background:linear-gradient(180deg,#f3e6d3,#8cbf5a)}
  .footer{position:absolute;left:0;top:1085px;width:854px;height:115px;background:var(--white);display:flex;align-items:center;padding:0 28px}
  .brand{width:300px}
  .brand-en{font-size:12px;letter-spacing:2px;color:var(--green-dark);font-weight:700}
  .brand-name{display:flex;align-items:center;gap:10px;font-size:38px;font-weight:900;color:var(--green-dark);line-height:48px}
  .brand-mark{width:30px;height:30px;border-radius:50%;background:var(--green)}
  .brand-tag{font-size:13px;color:var(--text)}
  .contact{margin-left:auto;width:480px}
  .contact-note{display:flex;gap:10px;font-size:15px;font-weight:700}
  .contact-note .pill{background:var(--orange);color:var(--white);padding:1px 10px;border-radius:10px;font-size:13px}
  .contact-note .lead{color:var(--orange)}
  .phone{display:flex;align-items:center;gap:12px}
  .phone-mark{width:52px;height:40px;background:var(--green-dark);border-radius:4px}
  .phone-number{font-size:50px;font-weight:900;letter-spacing:1px;color:var(--brown);line-height:58px}
  .hours{font-size:12px;color:var(--text)}
</style>
</head>
<body>
<main class="flyer">
  <div class="hero-photo" role="img" aria-label="庭で手袋をして雑草を抜く人の手元と芝生の写真"></div>
  <div class="grass-strip" role="img" aria-label="草の縁どり"></div>

  <div class="badge">除草だけでも<br>承ります!</div>

  <h1 class="headline">
    <div class="line1">お庭の<span class="accent">雑草</span></div>
    <div class="line2">お困りではありませんか?</div>
  </h1>

  <div class="before" role="img" aria-label="除草前の雑草が茂った庭の写真"><span class="tag">Before</span></div>
  <div class="after" role="img" aria-label="除草後のすっきりした庭の写真"><span class="tag">After</span></div>
  <svg class="arrow" width="80" height="70" viewBox="0 0 80 70" aria-hidden="true">
    <path d="M0 20 H42 V0 L80 35 L42 70 V50 H0 Z" fill="#f08a1c" stroke="#fff" stroke-width="4"/>
  </svg>

  <section class="check-panel">
    <h2 class="check-title">お庭の<span class="accent">雑草</span> お困りごとチェック</h2>
    <ul class="check-list">
      <li><svg width="24" height="24" viewBox="0 0 24 24"><rect x="1" y="1" width="22" height="22" rx="3" fill="#fff" stroke="#6fae3a" stroke-width="2"/><path d="M5 12 L10 17 L19 6" fill="none" stroke="#f08a1c" stroke-width="3"/></svg>仕事が忙しくて草むしりする時間が取れない。</li>
      <li><svg width="24" height="24" viewBox="0 0 24 24"><rect x="1" y="1" width="22" height="22" rx="3" fill="#fff" stroke="#6fae3a" stroke-width="2"/><path d="M5 12 L10 17 L19 6" fill="none" stroke="#f08a1c" stroke-width="3"/></svg>少し前まで自分でやっていたが体力的に難しくなった。</li>
      <li><svg width="24" height="24" viewBox="0 0 24 24"><rect x="1" y="1" width="22" height="22" rx="3" fill="#fff" stroke="#6fae3a" stroke-width="2"/><path d="M5 12 L10 17 L19 6" fill="none" stroke="#f08a1c" stroke-width="3"/></svg>親が他界して相続した家。自分は庭に興味ない。</li>
      <li><svg width="24" height="24" viewBox="0 0 24 24"><rect x="1" y="1" width="22" height="22" rx="3" fill="#fff" stroke="#6fae3a" stroke-width="2"/><path d="M5 12 L10 17 L19 6" fill="none" stroke="#f08a1c" stroke-width="3"/></svg>お隣さんから苦情がきてしまう。</li>
    </ul>
    <div class="figure-slot" role="img" aria-label="困った様子の年配男性のイラスト"></div>
  </section>

  <footer class="footer">
    <div class="brand">
      <div class="brand-en">NIWAMORI KOUBOU</div>
      <div class="brand-name"><span class="brand-mark"></span>庭守工房</div>
      <div class="brand-tag">私たちは日本のお庭を元気にします</div>
    </div>
    <div class="contact">
      <div class="contact-note"><span class="pill">通話無料</span><span class="lead">お見積り無料 お気軽にご相談ください!</span></div>
      <div class="phone"><span class="phone-mark"></span><span class="phone-number">0120-574-861</span></div>
      <div class="hours">[受付] 9:00〜18:00 土日・祝日も受付(年末年始除く)</div>
    </div>
  </footer>
</main>
</body>
</html>
```